Web Design for Financial Consulting Company

We need a website design for a financial consulting company "Korvane Consulting". We build financial models, scenario analysis, handle the budgeting process and provide temporary staffing. I have over 10 years of experience. My Excel expertise and analytical savvy has saved clients over $17 million in profit.

Target Market(s)

Small to medium businesses

Industry/Entity Type

Financial Consulting

Number of Pages Required

4 page

Requirements
Must have
• Professional looking
Nice to have
• A little futuristic looking

```html
<!DOCTYPE html>
<html lang="en">
<head>
<meta charset="utf-8">
<title>Korvane Consulting — Home Page Presentation</title>
<link rel="stylesheet" href="https://fonts.googleapis.com/css2?family=Cinzel:wght@500;600&family=Lexend:wght@300;400;500;600&family=Great+Vibes&display=swap">
<style>
:root{
  --blue:#0b9be8;
  --blue-light:#2cb2f4;
  --hero:#03060a;
  --panel:#16212c;
  --panel-2:#18232e;
  --foot:#1a2631;
  --nav:#111a23;
  --ink:#14202b;
  --muted:#a9b6c2;
  --grey:#6a7580;
  --white:#ffffff;
  --line:#8593a0;
}
*{box-sizing:border-box;margin:0;padding:0}
html,body{width:1200px;height:3632px;overflow:hidden}
body{font-family:'Lexend',sans-serif;color:var(--white)}
.board{position:relative;width:1200px;height:3632px;overflow:hidden;
  background:linear-gradient(115deg,#15212b 0%,#12303f 30%,#0a6fae 62%,#079ce8 85%,#0aa6f0 100%)}

/* ===== Presentation headings ===== */
.board-title{position:absolute;left:0;width:1200px;top:706px;text-align:center;font-family:'Cinzel',serif;font-weight:600;font-size:64px;letter-spacing:3px;color:var(--white)}
.board-label{position:absolute;font-family:'Cinzel',serif;font-weight:500;color:var(--white);letter-spacing:2px;background:none}
.board-label.mobile-label{left:88px;top:822px;font-size:33px}
.board-label.web-label{left:580px;top:806px;font-size:64px;letter-spacing:3px}
.thanks{position:absolute;left:0;width:1200px;top:3478px;text-align:center;font-family:'Great Vibes',cursive;font-size:92px;color:var(--white)}

/* ===== Screen previews ===== */
.screen{position:absolute;overflow:hidden;background:var(--hero)}
.screen.laptop{left:465px;top:70px;width:576px;height:367px}
.screen.tablet{left:141px;top:148px;width:289px;height:385px}
.screen.phone{left:355px;top:282px;width:167px;height:345px;border-radius:10px;box-shadow:0 0 0 3px #0d141b}
.screen .web{position:absolute;left:0;top:0}
.screen.tablet .web{transform:scale(.5);transform-origin:0 0}
.screen.phone .mob{position:absolute;left:0;top:0;transform:scale(1.37);transform-origin:0 0}

/* ===== Web page ===== */
.web{position:absolute;left:517px;width:576px;background:var(--panel);overflow:hidden;font-family:'Lexend',sans-serif}
.topbar{height:12px;position:relative;background:linear-gradient(100deg,var(--blue) 0 50%,var(--nav) 50%)}
.socials{position:absolute;left:78px;top:2.5px;display:flex;gap:3px}
.socials i{display:block;width:7px;height:7px;background:var(--white);border-radius:1px}
.top-contact{position:absolute;right:80px;top:3px;display:flex;gap:10px;font-size:4.5px;color:var(--white)}
.nav{height:34px;position:relative;background:var(--nav);font-size:5.5px}
.nav a{position:absolute;top:14px;color:var(--white);text-decoration:none}
.nav .logo{position:absolute;left:244px;top:9px}
.nav .cta{top:10px;left:447px;border:1px solid var(--blue);padding:3px 6px;font-size:4.5px;color:var(--white)}
.logo{display:flex;align-items:center;gap:3px;color:var(--white)}
.logo-mark{width:11px;height:11px;border:1.5px solid currentColor}
.logo-text{display:flex;flex-direction:column;line-height:1;font-weight:600}
.logo-text b{font-size:9px;font-weight:600;letter-spacing:.3px}
.logo-text small{font-size:3.5px;font-weight:600;letter-spacing:2.6px;margin-top:1px}

.hero{height:270px;position:relative;background:var(--hero);overflow:hidden}
.hero-art{position:absolute;right:0;top:0;width:380px;height:270px;
  background:radial-gradient(ellipse 60% 45% at 55% 78%,rgba(26,170,255,.75),rgba(7,60,120,.35) 55%,transparent 75%),
             linear-gradient(180deg,#03060a 0%,#041427 60%,#03060a 100%)}
.hero-title{position:absolute;left:75px;top:58px;font-size:20px;line-height:25px;font-weight:500;text-transform:uppercase;color:var(--white);letter-spacing:.3px}
.hero-title em{font-style:normal;color:var(--blue)}
.hero-desc{position:absolute;left:76px;top:138px;width:220px;font-size:4.5px;line-height:7px;color:var(--muted)}
.btn{display:inline-block;background:var(--blue);color:var(--white);font-size:4px;font-weight:500;text-transform:uppercase;text-align:center;letter-spacing:.2px}
.btn-outline{display:inline-block;border:1px solid var(--blue);color:var(--white);font-size:4px;font-weight:500;text-transform:uppercase;text-align:center}
.hero .btn{position:absolute;left:76px;top:166px;width:50px;height:11px;line-height:11px}
.dots{position:absolute;left:24px;top:106px;display:flex;flex-direction:column;gap:5px}
.dots i{display:block;width:3px;height:3px;border-radius:50%;background:var(--white)}
.dots i.on{background:var(--blue)}

.services{height:283px;position:relative;background:var(--panel);text-align:center;padding-top:28px}
.sec-title{font-size:18px;font-weight:500;text-transform:uppercase;line-height:20px;letter-spacing:.5px}
.sec-sub{font-size:4px;letter-spacing:4px;color:var(--blue);text-transform:uppercase;margin-top:2px}
.cards{display:flex;justify-content:center;gap:10px;margin-top:10px}
.card{width:97px}
.card-img{height:92px}
.card h3{font-size:5.5px;font-weight:500;text-transform:uppercase;margin:8px 0 3px}
.card p{font-size:4px;line-height:6px;color:var(--muted)}
.card .btn-outline,.card .btn{width:46px;height:10px;line-height:8px;margin-top:6px}
.card .btn{line-height:10px}
.view-all{width:60px;height:11px;line-height:11px;margin-top:14px}
.img-models{background:linear-gradient(135deg,#0b1a3d 0%,#1d3f8a 55%,#3a7ee0 100%)}
.img-budget{background:linear-gradient(180deg,#c98fd0 0%,#6e6fc9 35%,#2b5fb5 70%,#1a2f6e 100%)}
.img-staffing{background:linear-gradient(160deg,#0c1f2c 0%,#0f3b4a 50%,#1a6b5b 100%)}
.img-cleansing{background:linear-gradient(180deg,#1d2b36 0%,#2b6f78 55%,#7fd6c9 100%)}

.about{height:224px;position:relative;background:linear-gradient(90deg,#0a85cf 0%,#0b9be8 55%,#18aef3 100%)}
.about-img{position:absolute;left:78px;top:28px;width:166px;height:155px;background:linear-gradient(140deg,#071a36 0%,#0b3b78 50%,#2c8fe0 100%);border:1px solid rgba(255,255,255,.6)}
.about-badge{position:absolute;left:206px;top:144px;width:48px;height:45px;background:var(--white);border:2px solid var(--blue)}
.about-badge i{position:absolute;left:12px;top:11px;width:22px;height:20px;border:2px solid var(--blue)}
.about-text{position:absolute;left:279px;top:36px;width:240px}
.about-text h2{font-size:17px;line-height:18px;font-weight:400;text-transform:uppercase;letter-spacing:.4px}
.about-text .sec-sub{color:var(--white);margin:6px 0 6px}
.about-text p{font-size:4px;line-height:6px;color:#e3f3fd;margin-bottom:8px}
.about-text .btn-outline{border-color:var(--white);width:44px;height:10px;line-height:8px}

.contact{height:203px;position:relative;background:var(--panel-2);text-align:center;padding-top:26px}
.contact-info{position:absolute;left:78px;top:80px;text-align:left;font-size:4.5px;line-height:7px}
.contact-info li{list-style:none;display:flex;gap:6px;align-items:flex-start;margin-bottom:9px}
.contact-info svg{flex:none;width:8px;height:8px}
.form{position:absolute;left:244px;top:70px;width:254px;display:grid;grid-template-columns:1fr 1fr;gap:6px 6px;text-align:left}
.field{height:18px;border:1px solid var(--line);font-size:3.5px;color:var(--muted);padding:3px 4px}
.field.msg{grid-column:1/3;height:40px}
.contact .btn{position:absolute;left:347px;top:177px;width:48px;height:10px;line-height:10px}

.footer{height:175px;position:relative;background:var(--foot);text-align:center}
.footer .logo{position:absolute;left:232px;top:22px}
.footer .logo .logo-mark{width:14px;height:14px}
.footer .logo-text b{font-size:12px}
.footer .logo-text small{font-size:4.5px;letter-spacing:3.4px}
.foot-items{position:absolute;left:88px;top:64px;width:420px;display:flex;justify-content:space-between;text-align:left;font-size:4.5px;line-height:6px}
.foot-items div{display:flex;gap:6px;align-items:center}
.foot-items .ic{width:14px;height:14px;border-radius:50%;background:var(--blue);flex:none}
.foot-rule{position:absolute;left:78px;right:78px;top:100px;height:1px;background:#5b6875}
.foot-links{position:absolute;left:0;right:0;top:106px;display:flex;justify-content:center;gap:14px;font-size:4.5px;font-weight:500;text-transform:uppercase}
.foot-rule.low{top:118px}
.copy{position:absolute;left:0;right:0;top:136px;font-size:4.5px;color:var(--muted)}
.foot-soc{position:absolute;left:0;right:0;top:148px;display:flex;justify-content:center;gap:4px}
.foot-soc i{width:7px;height:7px;background:var(--white);display:block}

/* light variant */
.web.light .topbar{background:linear-gradient(100deg,var(--blue) 0 50%,#0a8fd8 50%)}
.web.light .nav{background:var(--white)}
.web.light .nav a{color:var(--ink)}
.web.light .nav .logo{color:var(--ink)}
.web.light .nav .cta{color:var(--ink)}
.web.light .services,.web.light .contact{background:var(--white);color:var(--ink)}
.web.light .card p{color:var(--grey)}
.web.light .card .btn-outline,.web.light .services .sec-title,.web.light .contact .sec-title{color:var(--ink)}
.web.light .field{border-color:#9aa5ae;color:var(--grey)}
.web.light .contact-info{color:var(--ink)}

/* ===== Mobile page ===== */
.mob{position:absolute;left:164px;top:914px;width:122px;height:1850px;background:var(--white);overflow:hidden;color:var(--ink)}
.mob-head{height:17px;position:relative;background:var(--white)}
.mob-head .logo{position:absolute;left:4px;top:3px;color:var(--ink)}
.mob-head .logo-mark{width:9px;height:9px}
.mob-head .logo-text b{font-size:7.5px}
.mob-head .logo-text small{font-size:2.8px;letter-spacing:2px}
.burger{position:absolute;right:5px;top:6px;width:6px;display:flex;flex-direction:column;gap:1.3px}
.burger i{display:block;height:1px;background:var(--ink)}
.mob-hero{height:136px;position:relative;background:var(--hero);overflow:hidden;text-align:center}
.mob-hero .hero-art{width:122px;height:80px;top:56px;right:0}
.mob-hero h1{position:relative;padding-top:8px;font-size:8.5px;line-height:10.5px;font-weight:500;text-transform:uppercase;color:var(--white)}
.mob-hero h1 em{font-style:normal;color:var(--blue)}
.mob-hero .btn{position:relative;width:28px;height:6px;line-height:6px;font-size:2.5px;margin-top:3px}
.mob-dots{position:absolute;left:0;right:0;bottom:4px;display:flex;justify-content:center;gap:3px}
.mob-dots i{width:3px;height:3px;border-radius:50%;background:var(--white)}
.mob-dots i.on{background:var(--blue)}
.mob-services{height:760px;text-align:center;padding-top:20px}
.mob .sec-title{font-size:10px;line-height:12px}
.mob .sec-sub{font-size:2.6px;letter-spacing:2.5px;margin-top:1px}
.mob-card{width:99px;margin:9px auto 0}
.mob-card + .mob-card{margin-top:17px}
.mob-card .card-img{height:92px}
.mob-card h3{font-size:5px;font-weight:500;text-transform:uppercase;margin:7px 0 2px}
.mob-card p{font-size:3.6px;line-height:5.5px;color:var(--grey)}
.mob-card .btn-outline,.mob-card .btn{width:44px;height:10px;line-height:8px;margin-top:5px;color:var(--ink);font-size:3.2px}
.mob-card .btn{line-height:10px;color:var(--white)}
.mob .view-all{width:58px;height:10px;line-height:10px;margin-top:18px;font-size:3.2px}
.mob-about{height:359px;position:relative;background:linear-gradient(90deg,#0a85cf,#14a8f0);text-align:center;color:var(--white);padding:18px 9px 0}
.mob-about h2{font-size:9px;line-height:10px;font-weight:400;text-transform:uppercase}
.mob-about .sec-sub{color:var(--white);margin:6px 0}
.mob-about p{font-size:3.6px;line-height:6px;margin-bottom:8px;color:#e3f3fd}
.mob-about .btn-outline{border-color:var(--white);width:40px;height:9px;line-height:7px;font-size:3px}
.mob-about .about-img{left:11px;top:230px;width:99px;height:100px}
.mob-about .about-badge{left:86px;top:306px;width:28px;height:27px}
.mob-about .about-badge i{left:6px;top:6px;width:12px;height:11px}
.mob-contact{height:314px;position:relative;background:var(--white);text-align:center;padding-top:18px}
.mob-contact .contact-info{left:8px;top:44px;color:var(--ink);font-size:3.8px;line-height:6px}
.mob-contact .contact-info li{margin-bottom:12px}
.mob-form{position:absolute;left:8px;top:126px;width:106px}
.mob-form .field{height:15px;border-color:#9aa5ae;margin-bottom:10px;font-size:3px}
.mob-form .field.msg{height:38px}
.mob-contact .btn{position:absolute;left:38px;top:277px;width:46px;height:8px;line-height:8px;font-size:3px}
.mob-foot{height:264px;position:relative;background:var(--foot);color:var(--white);text-align:center}
.mob-foot .logo{position:absolute;left:20px;top:16px}
.mob-foot .logo-text b{font-size:9px}
.mob-foot .logo-text small{font-size:3px;letter-spacing:2.7px}
.mob-foot-items{position:absolute;left:10px;top:44px;text-align:left;font-size:3.8px;line-height:5px}
.mob-foot-items div{display:flex;gap:5px;align-items:center;margin-bottom:9px}
.mob-foot-items .ic{width:11px;height:11px;border-radius:50%;background:var(--blue);flex:none}
.mob-foot-links{position:absolute;left:0;right:0;top:124px;font-size:4px;font-weight:500;text-transform:uppercase;line-height:14px}
.mob-foot .rule{position:absolute;left:10px;right:10px;top:212px;height:1px;background:#5b6875}
.mob-foot .copy{top:218px;font-size:3.2px;line-height:5px}
.mob-foot .foot-soc{top:242px}
</style>
</head>
<body>
<main class="board">

  <!-- Screen previews -->
  <div class="screen laptop">
    <div class="web light">
      <div class="topbar"><div class="socials"><i></i><i></i><i></i><i></i></div><div class="top-contact"><span>+1 555 010 2040</span><span>info@korvaneconsulting.com</span></div></div>
      <header class="nav"><a style="left:78px">Home</a><a style="left:118px">About Us</a><a style="left:165px">Our Services</a>
        <div class="logo"><i class="logo-mark"></i><span class="logo-text"><b>KORVANE</b><small>Consulting</small></span></div>
        <a style="left:364px">Blog</a><a style="left:398px">Contact Us</a><a class="cta">Get in touch</a></header>
      <section class="hero">
        <div class="hero-art" role="img" aria-label="Glowing blue 3D bar chart rising from a dark floor"></div>
        <div class="dots"><i></i><i></i><i></i><i></i><i class="on"></i></div>
        <h1 class="hero-title">Helping <em>your</em><br><em>finance team</em> and<br>increasing profit.</h1>
        <p class="hero-desc">Clear models and steady budgets that help growing businesses plan ahead and keep more of what they earn.</p>
        <span class="btn">Get started</span>
      </section>
      <section class="services"><h2 class="sec-title">Our Services</h2></section>
    </div>
  </div>

  <div class="screen tablet">
    <div class="web">
      <div class="topbar"><div class="socials"><i></i><i></i><i></i><i></i></div><div class="top-contact"><span>+1 555 010 2040</span><span>info@korvaneconsulting.com</span></div></div>
      <header class="nav"><a style="left:78px">Home</a><a style="left:118px">About Us</a><a style="left:165px">Our Services</a>
        <div class="logo"><i class="logo-mark"></i><span class="logo-text"><b>KORVANE</b><small>Consulting</small></span></div>
        <a style="left:364px">Blog</a><a style="left:398px">Contact Us</a><a class="cta">Get in touch</a></header>
      <section class="hero">
        <div class="hero-art" role="img" aria-label="Glowing blue 3D bar chart rising from a dark floor"></div>
        <div class="dots"><i></i><i></i><i></i><i></i><i class="on"></i></div>
        <h1 class="hero-title">Helping <em>your</em><br><em>finance team</em> and<br>increasing profit.</h1>
        <p class="hero-desc">Clear models and steady budgets that help growing businesses plan ahead and keep more of what they earn.</p>
        <span class="btn">Get started</span>
      </section>
      <section class="services">
        <h2 class="sec-title">Our Services</h2><p class="sec-sub">What we do</p>
        <div class="cards">
          <div class="card"><div class="card-img img-models" role="img" aria-label="Rising financial graph on a blue screen"></div><h3>Financial Models</h3><p>Forecasts built in spreadsheets that show where your cash is heading.</p><span class="btn-outline">Learn more</span></div>
          <div class="card"><div class="card-img img-budget" role="img" aria-label="City skyline at dusk with data overlay"></div><h3>Budgeting Process</h3><p>A clear yearly budget with owners, targets and regular reviews.</p><span class="btn">Learn more</span></div>
          <div class="card"><div class="card-img img-staffing" role="img" aria-label="Green and blue trend lines on a dark screen"></div><h3>Temporary Staffing</h3><p>Skilled finance help for busy seasons, leave or open roles.</p><span class="btn-outline">Learn more</span></div>
          <div class="card"><div class="card-img img-cleansing" role="img" aria-label="Analytics dashboard with bar charts on a laptop"></div><h3>Data Cleansing</h3><p>Tidy, checked records so every report starts from solid data.</p><span class="btn-outline">Learn more</span></div>
        </div>
        <span class="btn view-all">View all services</span>
      </section>
      <section class="about">
        <div class="about-img" role="img" aria-label="Blue financial chart with glowing data lines"></div>
        <div class="about-badge"><i></i></div>
        <div class="about-text"><h2>About Korvane<br>Consulting.</h2><p class="sec-sub">Who we are</p></div>
      </section>
    </div>
  </div>

  <div class="screen phone">
    <div class="mob" style="left:0;top:0">
      <div class="mob-head"><div class="logo"><i class="logo-mark"></i><span class="logo-text"><b>KORVANE</b><small>Consulting</small></span></div><div class="burger"><i></i><i></i><i></i></div></div>
      <section class="mob-hero">
        <div class="hero-art" role="img" aria-label="Glowing blue 3D bar chart"></div>
        <h1>Helping <em>your</em><br><em>finance team</em> and<br>increasing profit.</h1>
        <span class="btn">Get started</span>
        <div class="mob-dots"><i></i><i></i><i></i><i class="on"></i><i></i></div>
      </section>
      <section class="mob-services">
        <h2 class="sec-title">Our Services</h2><p class="sec-sub">What we do</p>
        <div class="mob-card"><div class="card-img img-models" role="img" aria-label="Rising financial graph on a blue screen"></div></div>
      </section>
    </div>
  </div>

  <!-- Headings -->
  <h1 class="board-title">Home Page</h1>
  <h2 class="board-label mobile-label">Mobile Version</h2>
  <h2 class="board-label web-label">Web Version</h2>

  <!-- Mobile version -->
  <div class="mob">
    <div class="mob-head"><div class="logo"><i class="logo-mark"></i><span class="logo-text"><b>KORVANE</b><small>Consulting</small></span></div><div class="burger"><i></i><i></i><i></i></div></div>
    <section class="mob-hero">
      <div class="hero-art" role="img" aria-label="Glowing blue 3D bar chart"></div>
      <h1>Helping <em>your</em><br><em>finance team</em> and<br>increasing profit.</h1>
      <span class="btn">Get started</span>
      <div class="mob-dots"><i></i><i></i><i></i><i class="on"></i><i></i></div>
    </section>
    <section class="mob-services">
      <h2 class="sec-title">Our Services</h2><p class="sec-sub">What we do</p>
      <div class="mob-card"><div class="card-img img-models" role="img" aria-label="Rising financial graph on a blue screen"></div><h3>Financial Models</h3><p>Forecasts built in spreadsheets that show where your cash is heading.</p><span class="btn-outline">Learn more</span></div>
      <div class="mob-card"><div class="card-img img-budget" role="img" aria-label="City skyline at dusk with data overlay"></div><h3>Budgeting Process</h3><p>A clear yearly budget with owners, targets and regular reviews.</p><span class="btn">Learn more</span></div>
      <div class="mob-card"><div class="card-img img-staffing" role="img" aria-label="Green and blue trend lines on a dark screen"></div><h3>Temporary Staffing</h3><p>Skilled finance help for busy seasons, leave or open roles.</p><span class="btn-outline">Learn more</span></div>
      <div class="mob-card"><div class="card-img img-cleansing" role="img" aria-label="Analytics dashboard with bar charts on a laptop"></div><h3>Data Cleansing</h3><p>Tidy, checked records so every report starts from solid data.</p><span class="btn-outline">Learn more</span></div>
      <span class="btn view-all">View all services</span>
    </section>
    <section class="mob-about">
      <h2>About Korvane<br>Consulting.</h2><p class="sec-sub">Who we are</p>
      <p>I am a finance consultant with over ten years of practice in models, scenario analysis and budgets. My spreadsheet skill and sharp analysis have saved clients over $17M in profit.</p>
      <p>We work with small and medium businesses to turn raw numbers into plans, giving owners a clear view of risk, cash and growth, and the confidence to act on it.</p>
      <span class="btn-outline">Learn more</span>
      <div class="about-img" role="img" aria-label="Blue financial chart with glowing data lines"></div>
      <div class="about-badge"><i></i></div>
    </section>
    <section class="mob-contact">
      <h2 class="sec-title">Contact Us</h2><p class="sec-sub">Get in touch</p>
      <ul class="contact-info">
        <li><svg viewBox="0 0 10 10"><path d="M5 0.5a3.3 3.3 0 0 0-3.3 3.3C1.7 6.3 5 9.5 5 9.5s3.3-3.2 3.3-5.7A3.3 3.3 0 0 0 5 .5z" fill="#0b9be8"/><circle cx="5" cy="3.8" r="1.2" fill="#fff"/></svg><span>120 Harbor Lane, Suite 4,<br>Riverton, CA 90210</span></li>
        <li><svg viewBox="0 0 10 10"><path d="M2 1l2 .3.6 2-1.2.9a6 6 0 0 0 2.4 2.4l.9-1.2 2 .6L9 8c-.3.7-1 1-1.7.9C4.4 8.5 1.5 5.6 1.1 2.7 1 2 1.3 1.3 2 1z" fill="#0b9be8"/></svg><span>+1 555 010 2040</span></li>
        <li><svg viewBox="0 0 10 10"><rect x=".8" y="2" width="8.4" height="6" fill="#0b9be8"/><path d="M.8 2L5 5.5 9.2 2" stroke="#fff" stroke-width=".8" fill="none"/></svg><span>info@korvaneconsulting.com</span></li>
      </ul>
      <div class="mob-form"><div class="field">First Name</div><div class="field">Last Name</div><div class="field">Email Address</div><div class="field">Phone Number</div><div class="field msg">Message</div></div>
      <span class="btn">Submit now</span>
    </section>
    <footer class="mob-foot">
      <div class="logo"><i class="logo-mark"></i><span class="logo-text"><b>KORVANE</b><small>Consulting</small></span></div>
      <div class="mob-foot-items">
        <div><i class="ic"></i><span>120 Harbor Lane, Suite 4,<br>Riverton, CA 90210</span></div>
        <div><i class="ic"></i><span>Telephone: +1 555 010 2040</span></div>
        <div><i class="ic"></i><span>Email Us<br>info@korvaneconsulting.com</span></div>
      </div>
      <nav class="mob-foot-links">Home<br>About Us<br>Our Services<br>Blog<br>Contact<br>Careers</nav>
      <div class="rule"></div>
      <p class="copy">Copyright © 2023 Korvane Consulting.<br>All Rights Reserved</p>
      <div class="foot-soc"><i></i><i></i><i></i><i></i></div>
    </footer>
  </div>

  <!-- Web version, dark -->
  <div class="web" style="top:931px">
    <div class="topbar"><div class="socials"><i></i><i></i><i></i><i></i></div><div class="top-contact"><span>+1 555 010 2040</span><span>info@korvaneconsulting.com</span></div></div>
    <header class="nav"><a style="left:78px">Home</a><a style="left:118px">About Us</a><a style="left:165px">Our Services</a>
      <div class="logo"><i class="logo-mark"></i><span class="logo-text"><b>KORVANE</b><small>Consulting</small></span></div>
      <a style="left:364px">Blog</a><a style="left:398px">Contact Us</a><a class="cta">Get in touch</a></header>
    <section class="hero">
      <div class="hero-art" role="img" aria-label="Glowing blue 3D bar chart rising from a dark floor"></div>
      <div class="dots"><i></i><i></i><i></i><i></i><i class="on"></i></div>
      <h1 class="hero-title">Helping <em>your</em><br><em>finance team</em> and<br>increasing profit.</h1>
      <p class="hero-desc">Clear models and steady budgets that help growing businesses plan ahead and keep more of what they earn.</p>
      <span class="btn">Get started</span>
    </section>
    <section class="services">
      <h2 class="sec-title">Our Services</h2><p class="sec-sub">What we do</p>
      <div class="cards">
        <div class="card"><div class="card-img img-models" role="img" aria-label="Rising financial graph on a blue screen"></div><h3>Financial Models</h3><p>Forecasts built in spreadsheets that show where your cash is heading.</p><span class="btn-outline">Learn more</span></div>
        <div class="card"><div class="card-img img-budget" role="img" aria-label="City skyline at dusk with data overlay"></div><h3>Budgeting Process</h3><p>A clear yearly budget with owners, targets and regular reviews.</p><span class="btn">Learn more</span></div>
        <div class="card"><div class="card-img img-staffing" role="img" aria-label="Green and blue trend lines on a dark screen"></div><h3>Temporary Staffing</h3><p>Skilled finance help for busy seasons, leave or open roles.</p><span class="btn-outline">Learn more</span></div>
        <div class="card"><div class="card-img img-cleansing" role="img" aria-label="Analytics dashboard with bar charts on a laptop"></div><h3>Data Cleansing</h3><p>Tidy, checked records so every report starts from solid data.</p><span class="btn-outline">Learn more</span></div>
      </div>
      <span class="btn view-all">View all services</span>
    </section>
    <section class="about">
      <div class="about-img" role="img" aria-label="Blue financial chart with glowing data lines"></div>
      <div class="about-badge"><i></i></div>
      <div class="about-text"><h2>About Korvane<br>Consulting.</h2><p class="sec-sub">Who we are</p>
        <p>I am a finance consultant with over ten years of practice in models, scenario analysis and budgets. My spreadsheet skill and sharp analysis have saved clients over $17M in profit.</p>
        <p>We work with small and medium businesses to turn raw numbers into plans, giving owners a clear view of risk, cash and growth.</p>
        <span class="btn-outline">Learn more</span></div>
    </section>
    <section class="contact">
      <h2 class="sec-title">Contact Us</h2><p class="sec-sub">Get in touch</p>
      <ul class="contact-info">
        <li><svg viewBox="0 0 10 10"><path d="M5 0.5a3.3 3.3 0 0 0-3.3 3.3C1.7 6.3 5 9.5 5 9.5s3.3-3.2 3.3-5.7A3.3 3.3 0 0 0 5 .5z" fill="#0b9be8"/><circle cx="5" cy="3.8" r="1.2" fill="#fff"/></svg><span>120 Harbor Lane, Suite 4,<br>Riverton, CA 90210</span></li>
        <li><svg viewBox="0 0 10 10"><path d="M2 1l2 .3.6 2-1.2.9a6 6 0 0 0 2.4 2.4l.9-1.2 2 .6L9 8c-.3.7-1 1-1.7.9C4.4 8.5 1.5 5.6 1.1 2.7 1 2 1.3 1.3 2 1z" fill="#0b9be8"/></svg><span>+1 555 010 2040</span></li>
        <li><svg viewBox="0 0 10 10"><rect x=".8" y="2" width="8.4" height="6" fill="#0b9be8"/><path d="M.8 2L5 5.5 9.2 2" stroke="#fff" stroke-width=".8" fill="none"/></svg><span>info@korvaneconsulting.com</span></li>
      </ul>
      <div class="form"><div class="field">First Name</div><div class="field">Last Name</div><div class="field">Email Address</div><div class="field">Phone Number</div><div class="field msg">Message</div></div>
      <span class="btn">Submit now</span>
    </section>
    <footer class="footer">
      <div class="logo"><i class="logo-mark"></i><span class="logo-text"><b>KORVANE</b><small>Consulting</small></span></div>
      <div class="foot-items">
        <div><i class="ic"></i><span>120 Harbor Lane, Suite 4,<br>Riverton, CA 90210</span></div>
        <div><i class="ic"></i><span>Telephone: +1 555 010 2040</span></div>
        <div><i class="ic"></i><span>Email Us<br>info@korvaneconsulting.com</span></div>
      </div>
      <div class="foot-rule"></div>
      <nav class="foot-links"><span>Home</span><span>About Us</span><span>Our Services</span><span>Blog</span><span>Contact</span><span>Careers</span></nav>
      <div class="foot-rule low"></div>
      <p class="copy">Copyright © 2023 Korvane Consulting. All Rights Reserved</p>
      <div class="foot-soc"><i></i><i></i><i></i><i></i></div>
    </footer>
  </div>

  <!-- Web version, light -->
  <div class="web light" style="top:2181px">
    <div class="topbar"><div class="socials"><i></i><i></i><i></i><i></i></div><div class="top-contact"><span>+1 555 010 2040</span><span>info@korvaneconsulting.com</span></div></div>
    <header class="nav"><a style="left:78px">Home</a><a style="left:118px">About Us</a><a style="left:165px">Our Services</a>
      <div class="logo"><i class="logo-mark"></i><span class="logo-text"><b>KORVANE</b><small>Consulting</small></span></div>
      <a style="left:364px">Blog</a><a style="left:398px">Contact Us</a><a class="cta">Get in touch</a></header>
    <section class="hero">
      <div class="hero-art" role="img" aria-label="Glowing blue 3D bar chart rising from a dark floor"></div>
      <div class="dots"><i></i><i></i><i></i><i></i><i class="on"></i></div>
      <h1 class="hero-title">Helping <em>your</em><br><em>finance team</em> and<br>increasing profit.</h1>
      <p class="hero-desc">Clear models and steady budgets that help growing businesses plan ahead and keep more of what they earn.</p>
      <span class="btn">Get started</span>
    </section>
    <section class="services">
      <h2 class="sec-title">Our Services</h2><p class="sec-sub">What we do</p>
      <div class="cards">
        <div class="card"><div class="card-img img-models" role="img" aria-label="Rising financial graph on a blue screen"></div><h3>Financial Models</h3><p>Forecasts built in spreadsheets that show where your cash is heading.</p><span class="btn-outline">Learn more</span></div>
        <div class="card"><div class="card-img img-budget" role="img" aria-label="City skyline at dusk with data overlay"></div><h3>Budgeting Process</h3><p>A clear yearly budget with owners, targets and regular reviews.</p><span class="btn">Learn more</span></div>
        <div class="card"><div class="card-img img-staffing" role="img" aria-label="Green and blue trend lines on a dark screen"></div><h3>Temporary Staffing</h3><p>Skilled finance help for busy seasons, leave or open roles.</p><span class="btn-outline">Learn more</span></div>
        <div class="card"><div class="card-img img-cleansing" role="img" aria-label="Analytics dashboard with bar charts on a laptop"></div><h3>Data Cleansing</h3><p>Tidy, checked records so every report starts from solid data.</p><span class="btn-outline">Learn more</span></div>
      </div>
      <span class="btn view-all">View all services</span>
    </section>
    <section class="about">
      <div class="about-img" role="img" aria-label="Blue financial chart with glowing data lines"></div>
      <div class="about-badge"><i></i></div>
      <div class="about-text"><h2>About Korvane<br>Consulting.</h2><p class="sec-sub">Who we are</p>
        <p>I am a finance consultant with over ten years of practice in models, scenario analysis and budgets. My spreadsheet skill and sharp analysis have saved clients over $17M in profit.</p>
        <p>We work with small and medium businesses to turn raw numbers into plans, giving owners a clear view of risk, cash and growth.</p>
        <span class="btn-outline">Learn more</span></div>
    </section>
    <section class="contact">
      <h2 class="sec-title">Contact Us</h2><p class="sec-sub">Get in touch</p>
      <ul class="contact-info">
        <li><svg viewBox="0 0 10 10"><path d="M5 0.5a3.3 3.3 0 0 0-3.3 3.3C1.7 6.3 5 9.5 5 9.5s3.3-3.2 3.3-5.7A3.3 3.3 0 0 0 5 .5z" fill="#0b9be8"/><circle cx="5" cy="3.8" r="1.2" fill="#fff"/></svg><span>120 Harbor Lane, Suite 4,<br>Riverton, CA 90210</span></li>
        <li><svg viewBox="0 0 10 10"><path d="M2 1l2 .3.6 2-1.2.9a6 6 0 0 0 2.4 2.4l.9-1.2 2 .6L9 8c-.3.7-1 1-1.7.9C4.4 8.5 1.5 5.6 1.1 2.7 1 2 1.3 1.3 2 1z" fill="#0b9be8"/></svg><span>+1 555 010 2040</span></li>
        <li><svg viewBox="0 0 10 10"><rect x=".8" y="2" width="8.4" height="6" fill="#0b9be8"/><path d="M.8 2L5 5.5 9.2 2" stroke="#fff" stroke-width=".8" fill="none"/></svg><span>info@korvaneconsulting.com</span></li>
      </ul>
      <div class="form"><div class="field">First Name</div><div class="field">Last Name</div><div class="field">Email Address</div><div class="field">Phone Number</div><div class="field msg">Message</div></div>
      <span class="btn">Submit now</span>
    </section>
    <footer class="footer">
      <div class="logo"><i class="logo-mark"></i><span class="logo-text"><b>KORVANE</b><small>Consulting</small></span></div>
      <div class="foot-items">
        <div><i class="ic"></i><span>120 Harbor Lane, Suite 4,<br>Riverton, CA 90210</span></div>
        <div><i class="ic"></i><span>Telephone: +1 555 010 2040</span></div>
        <div><i class="ic"></i><span>Email Us<br>info@korvaneconsulting.com</span></div>
      </div>
      <div class="foot-rule"></div>
      <nav class="foot-links"><span>Home</span><span>About Us</span><span>Our Services</span><span>Blog</span><span>Contact</span><span>Careers</span></nav>
      <div class="foot-rule low"></div>
      <p class="copy">Copyright © 2023 Korvane Consulting. All Rights Reserved</p>
      <div class="foot-soc"><i></i><i></i><i></i><i></i></div>
    </footer>
  </div>

  <p class="thanks">Thank You For Watching</p>
</main>
</body>
</html>
```